Box and label design for oil Tincture bottle

I need to design an attractive looking label for a 30ml CBD oil tincture along with designing a box for the tincture oil. I already have the logo (see attachment). I just need a nice, attractive looking artwork for the label and the box. The box is the standard 30ml tincture oil (see example attachment). The box has a total of 6 sides (4 on sides and 2 for top and bottom). Please include a section for supplemental facts and ingredients. Let's not focus to much on content. I am more concerned with design of box and label.
Target Market(s)
CBD customers

```html
<!DOCTYPE html>
<html lang="en">
<head>
<meta charset="utf-8">
<title>Bright Harbor CBD Oil Tincture – Box Dieline</title>
<link href="https://fonts.googleapis.com/css2?family=Montserrat:wght@400;500;600;700;800;900&family=Roboto+Condensed:wght@400;700&display=swap" rel="stylesheet">
<style>
  :root{
    --royal:#1f4fae;
    --sky:#1b8fd8;
    --ink:#2b2b2b;
    --paper:#f3f4f6;
    --swirl-a:#eceef1;
    --swirl-b:#dde1e6;
    --swirl-c:#d6e8f5;
    --cut:#d65a6a;
    --page:#ffffff;
  }
  html,body{margin:0;padding:0;overflow:hidden;}
  body{width:800px;height:1200px;background:var(--page);display:flex;align-items:center;justify-content:center;}
  .dieline{width:780px;height:938px;display:block;}
  .sans{font-family:"Montserrat",sans-serif;}
  .facts{font-family:"Roboto Condensed",sans-serif;}
  .cut{stroke:var(--cut);stroke-width:0.7;}
  .fold{stroke:var(--cut);stroke-width:0.4;stroke-dasharray:2 2;fill:none;}
  .royal{fill:var(--royal);}
  .sky{fill:var(--sky);}
  .ink{fill:var(--ink);}
  .white{fill:#fff;}
  .head{font-weight:700;font-size:11.5px;letter-spacing:.4px;}
  .body{font-weight:400;font-size:7.2px;}
  .brand{font-weight:700;font-size:10px;letter-spacing:-.2px;}
  .brand-sub{font-weight:600;font-size:5.5px;letter-spacing:1px;}
</style>
</head>
<body>
<svg class="dieline" viewBox="170 45 665 800" xmlns="http://www.w3.org/2000/svg">
  <defs>
    <linearGradient id="swirl" x1="0" y1="0" x2="1" y2="1">
      <stop offset="0" stop-color="var(--swirl-a)"/>
      <stop offset=".45" stop-color="var(--swirl-b)"/>
      <stop offset=".7" stop-color="var(--swirl-c)"/>
      <stop offset="1" stop-color="var(--swirl-a)"/>
    </linearGradient>

    <g id="front-face">
      <text class="sans ink" x="75" y="108" text-anchor="middle" font-weight="700" font-size="11.5" letter-spacing=".5">ALL NATURAL</text>
      <text class="sans sky" x="75" y="121" text-anchor="middle" font-weight="500" font-size="10.5" letter-spacing=".4">CBD 300 MG</text>
      <path class="royal" d="M0,387 L0,175 Q0,150 25,150 L34,150 Q59,150 59,175 L59,387 Z"/>
      <text class="sans white" transform="translate(54,381) rotate(-90)" font-weight="900" font-size="54" textLength="212" lengthAdjust="spacingAndGlyphs">CBD OIL</text>
      <text class="sans sky" transform="translate(90,381) rotate(-90)" font-weight="800" font-size="36" textLength="165" lengthAdjust="spacingAndGlyphs">TINCTURE</text>
      <g class="drop" transform="translate(134,356)">
        <path d="M0,0 C5,8 10,13 10,19 A10,10 0 0 1 -10,19 C-10,13 -5,8 0,0 Z" fill="#fff" stroke="var(--sky)" stroke-width="1.6"/>
        <text class="sans sky" x="0" y="21" text-anchor="middle" font-weight="800" font-size="8">30</text>
        <text class="sans sky" x="0" y="27" text-anchor="middle" font-weight="600" font-size="4.5">ml</text>
      </g>
    </g>
  </defs>

  <!-- background pattern surfaces -->
  <g role="img" aria-label="Light grey and pale blue swirling floral pattern covering the box surfaces" fill="url(#swirl)">
    <polygon class="cut" points="183,270 224,250 224,637 183,627"/>
    <rect class="cut" x="224" y="250" width="596" height="387"/>
    <polygon class="cut" points="373,250 373,122 493,122 522,240 522,250"/>
    <polygon class="cut" points="671,250 671,240 700,122 820,122 820,250"/>
    <polygon class="cut" points="373,637 522,637 522,650 493,767 373,767"/>
    <path class="cut" d="M522,637 L671,637 L671,800 Q671,830 641,830 L552,830 Q522,830 522,800 Z"/>
  </g>

  <!-- panel folds -->
  <line class="fold" x1="373" y1="250" x2="373" y2="637"/>
  <line class="fold" x1="522" y1="250" x2="522" y2="637"/>
  <line class="fold" x1="671" y1="250" x2="671" y2="637"/>
  <line class="fold" x1="522" y1="790" x2="671" y2="790"/>

  <!-- front panel with top tuck -->
  <g class="panel-front-a">
    <path class="royal cut" d="M224,90 Q224,57 257,57 L340,57 Q373,57 373,90 L373,250 A74.5,74.5 0 0 1 224,250 Z"/>
    <line x1="224" y1="97" x2="373" y2="97" stroke="#fff" stroke-opacity=".35" stroke-width=".6"/>
    <g class="brand-mark tuck" transform="rotate(180 299 172)">
      <circle cx="299" cy="156" r="12" fill="none" stroke="#fff" stroke-width="1.6"/>
      <text class="sans white brand" x="299" y="182" text-anchor="middle">BRIGHT HARBOR</text>
      <text class="sans white brand-sub" x="299" y="190" text-anchor="middle">CBD</text>
    </g>
    <g class="brand-mark">
      <circle cx="299" cy="278" r="12" fill="none" stroke="#fff" stroke-width="1.6"/>
      <text class="sans white brand" x="299" y="304" text-anchor="middle">BRIGHT HARBOR</text>
      <text class="sans white brand-sub" x="299" y="312" text-anchor="middle">CBD</text>
    </g>
    <use href="#front-face" x="224" y="250"/>
  </g>

  <!-- back panel: ingredients and facts -->
  <g class="panel-ingredients">
    <text class="sans royal head" x="447" y="288" text-anchor="middle">INGREDIENTS</text>
    <text class="sans ink body" text-anchor="middle">
      <tspan x="447" y="303">Lorem Ipsum has been the</tspan>
      <tspan x="447" y="312">industry's standard dummy text</tspan>
      <tspan x="447" y="321">ever since the 1500s. Lorem</tspan>
      <tspan x="447" y="330">Ipsum is simply dummy text of</tspan>
      <tspan x="447" y="339">the printing and typesetting</tspan>
      <tspan x="447" y="348">industry.</tspan>
    </text>
    <g class="facts supplement-facts">
      <rect x="383" y="385" width="130" height="144" fill="#fff" stroke="#222" stroke-width=".8"/>
      <text x="386" y="398" font-weight="700" font-size="12.5" fill="#111">Supplement Facts</text>
      <line x1="386" y1="401" x2="510" y2="401" stroke="#111" stroke-width=".5"/>
      <text x="386" y="408" font-size="4.5">Serving Size 1</text>
      <line x1="386" y1="411" x2="510" y2="411" stroke="#111" stroke-width="3"/>
      <text x="386" y="418" font-size="3.8" font-weight="700">Amount Per</text>
      <text x="386" y="422" font-size="3.8" font-weight="700">Capsule</text>
      <text x="510" y="418" font-size="3.8" font-weight="700" text-anchor="end">% Daily</text>
      <text x="510" y="422" font-size="3.8" font-weight="700" text-anchor="end">Value</text>
      <line x1="386" y1="426" x2="510" y2="426" stroke="#111" stroke-width="1.5"/>
      <g font-size="5">
        <text x="386" y="437">Calories  20</text>
        <text x="392" y="444">Calories from Fat  20</text>
        <text x="386" y="452">Total Fat  2 g</text><text x="510" y="452" text-anchor="end">3%*</text>
        <text x="392" y="460">Saturated Fat  0.5 g</text><text x="510" y="460" text-anchor="end">3%*</text>
        <text x="392" y="468">Polyunsaturated Fat  1 g</text><text x="510" y="468" text-anchor="end">†</text>
        <text x="392" y="476">Monounsaturated Fat  0.5 g</text><text x="510" y="476" text-anchor="end">†</text>
        <text x="386" y="484">Vitamin A  4250 IU</text><text x="510" y="484" text-anchor="end">85%</text>
        <text x="386" y="492">Vitamin D  425 IU</text><text x="510" y="492" text-anchor="end">106%</text>
        <text x="386" y="508">Omega-3 fatty acids  0.5 g</text><text x="510" y="508" text-anchor="end">†</text>
      </g>
      <g stroke="#111" stroke-width=".4">
        <line x1="386" y1="446" x2="510" y2="446"/><line x1="386" y1="454" x2="510" y2="454"/>
        <line x1="386" y1="462" x2="510" y2="462"/><line x1="386" y1="470" x2="510" y2="470"/>
        <line x1="386" y1="478" x2="510" y2="478"/><line x1="386" y1="486" x2="510" y2="486"/>
      </g>
      <line x1="386" y1="497" x2="510" y2="497" stroke="#111" stroke-width="2.5"/>
      <line x1="386" y1="513" x2="510" y2="513" stroke="#111" stroke-width="1.5"/>
      <text x="386" y="519" font-size="3.6">* Percent Daily Values based on a 2,000 calorie diet.</text>
      <text x="386" y="524" font-size="3.6">† Daily Value not established.</text>
    </g>
  </g>

  <!-- second front panel -->
  <g class="panel-front-b">
    <g class="brand-mark">
      <circle cx="597" cy="278" r="12" fill="none" stroke="var(--royal)" stroke-width="1.6"/>
      <text class="sans royal brand" x="597" y="304" text-anchor="middle">BRIGHT HARBOR</text>
      <text class="sans royal brand-sub" x="597" y="312" text-anchor="middle">CBD</text>
    </g>
    <use href="#front-face" x="522" y="250"/>
  </g>

  <!-- side panel: direction, storage, contact -->
  <g class="panel-direction">
    <text class="sans royal head" x="746" y="288" text-anchor="middle">DIRECTION</text>
    <text class="sans ink body" text-anchor="middle">
      <tspan x="746" y="303">Lorem Ipsum is simply dummy</tspan>
      <tspan x="746" y="312">text of the printing and</tspan>
      <tspan x="746" y="321">typesetting industry. Lorem</tspan>
      <tspan x="746" y="330">Ipsum has been the industry's</tspan>
      <tspan x="746" y="339">standard dummy text ever since</tspan>
      <tspan x="746" y="348">the 1500s</tspan>
    </text>
    <path class="royal" d="M671,637 L671,455 A74.5,74.5 0 0 1 820,455 L820,637 Z"/>
    <polygon class="royal cut" points="671,637 820,637 820,767 692,767"/>
    <text class="sans white head" text-anchor="middle" font-size="11">
      <tspan x="746" y="417">STORAGE</tspan>
      <tspan x="746" y="431">INSTRUCTION</tspan>
    </text>
    <text class="sans white body" text-anchor="middle">
      <tspan x="746" y="448">It is a long established fact that a</tspan>
      <tspan x="746" y="457">reader will be distracted by the</tspan>
      <tspan x="746" y="466">readable content of a page when</tspan>
      <tspan x="746" y="475">looking at its layout.</tspan>
    </text>
    <text class="sans white head" x="746" y="522" text-anchor="middle" font-size="11">CONTACT US</text>
    <text class="sans white body" text-anchor="middle">
      <tspan x="746" y="539">+100-555-0147</tspan>
      <tspan x="746" y="548">support@brightharbor.com</tspan>
      <tspan x="746" y="557">www.brightharbor.com</tspan>
    </text>
    <g class="white">
      <circle cx="729" cy="597" r="2.4"/><circle cx="746" cy="597" r="2.4"/><circle cx="763" cy="597" r="2.4"/>
    </g>
  </g>
</svg>
</body>
</html>
```